Tarnobe presentation

We built A 20-page powerpoint document. We would like to change the look of this document. We work in digital area. So, we would like something more modern, more current and less classical. We need to be fashionable while remaining reassuring for corporate. Our business is to make recommendations in 5 days where our competitors do it in 3 months.

Target Market(s)

medium sized business, or a large global enterprise

Industry/Entity Type

Digital

Colors

Designer to choose colors to be used in the design.

Requirements
Must have
• We are working with digital expert. We need to surprise them.

```html
<!DOCTYPE html>
<html lang="fr">
<head>
<meta charset="utf-8">
<title>Tarnobe — 360° Digital Sprint Assessment</title>
<link href="https://fonts.googleapis.com/css2?family=Bebas+Neue&family=Montserrat:wght@400;600;700&display=swap" rel="stylesheet">
<style>
:root{
  --navy:#1a1f3d; --navy-2:#2b3a6e; --white:#fff; --lime:#dde21b;
  --blue:#1f6fe8; --red:#e8283c; --orange:#f59a16; --green:#8cc63f;
  --pink:#e6197a; --magenta:#c62aa8; --purple:#6d3ccf; --cyan:#bdeefa;
  --sky:#2fa4ff; --muted:#c7cbe0;
}
*{margin:0;padding:0;box-sizing:border-box}
html,body{width:1200px;height:1200px;overflow:hidden;background:#fff}
body{position:relative;font-family:'Montserrat',sans-serif;color:var(--white)}
.page-number{position:absolute;right:22px;top:14px;font-family:'Bebas Neue',sans-serif;font-size:44px;color:#1d47b8}
.slide{position:absolute;width:274px;height:154px;overflow:hidden;
  background:radial-gradient(ellipse at 70% 20%,var(--navy-2),var(--navy) 75%)}
.c1{left:38px}.c2{left:320px}.c3{left:605px}.c4{left:890px}
.r1{top:93px}.r2{top:260px}.r3{top:431px}.r4{top:602px}.r5{top:772px}.r6{top:944px}
.brand{position:absolute;right:8px;bottom:7px;font:700 6px 'Montserrat',sans-serif;display:flex;align-items:center;gap:2px;z-index:2}
.brand::before{content:"";width:6px;height:6px;border-radius:50%;background:var(--white)}
.kicker{position:absolute;left:14px;top:14px;font:8px 'Bebas Neue',sans-serif;color:var(--lime)}
.title{position:absolute;left:14px;top:26px;font:20px/1.05 'Bebas Neue',sans-serif;letter-spacing:.2px}
.bebas{font-family:'Bebas Neue',sans-serif}
.runner-area{position:absolute;z-index:0;border-radius:40%;
  background:radial-gradient(ellipse at 50% 45%,rgba(230,25,122,.55),rgba(245,154,22,.35) 40%,rgba(109,60,207,0) 72%)}
.box{display:flex;align-items:center;justify-content:center;text-align:center;font:700 4px/1.3 'Montserrat',sans-serif;padding:2px}
.row{position:absolute;display:flex;gap:4px}
.quote{position:absolute;left:28px;font:24px/1.2 'Bebas Neue',sans-serif}
.big-num{position:absolute;left:38px;top:14px;font:150px/1 'Bebas Neue',sans-serif;color:var(--lime)}
.big-title{position:absolute;left:116px;font:32px/1 'Bebas Neue',sans-serif}
.tiny{font-size:3.4px;line-height:1.45;color:var(--muted)}
.expert{position:absolute;top:58px;width:118px;display:flex;gap:6px}
.photo{flex:none;width:32px;height:32px;border-radius:50%;border:2px solid var(--lime);background:radial-gradient(circle,#9a9a9a,#4a4a4a)}
.expert-name{font:700 4px 'Montserrat',sans-serif;color:var(--sky)}
.refs{position:absolute;font-size:3.6px;line-height:1.35}
.refs div{display:flex;margin-bottom:3px}
.refs b{flex:none;width:70px;color:var(--sky)}
.refs span{color:var(--muted)}
.front{z-index:1}
</style>
</head>
<body>
<div class="page-number">24</div>

<!-- Row 1 -->
<section class="slide c1 r1">
  <div class="runner-area" role="img" aria-label="Illustration d'un coureur en facettes colorées" style="left:180px;top:12px;width:80px;height:136px"></div>
  <div class="front" style="position:absolute;left:30px;top:14px;font:700 7px 'Montserrat',sans-serif;display:flex;align-items:center;gap:3px"><i style="width:9px;height:9px;border-radius:50%;background:#fff"></i>Tarnobe</div>
  <div class="bebas front" style="position:absolute;left:24px;top:52px;font-size:31px;line-height:1">360° Digital</div>
  <div class="bebas front" style="position:absolute;left:24px;top:84px;font-size:31px;line-height:1;color:var(--lime)">Sprint Assessment</div>
  <div class="bebas front" style="position:absolute;left:27px;top:126px;font-size:11px">13 juillet 2017</div>
</section>

<section class="slide c2 r1">
  <div class="quote" style="top:46px">« Le déni de voir<br>l'évolution est un délit! »</div>
  <div class="brand">Tarnobe</div>
</section>

<section class="slide c3 r1">
  <div class="runner-area" role="img" aria-label="Illustration d'un coureur en facettes colorées" style="left:175px;top:30px;width:70px;height:112px"></div>
  <div class="bebas front" style="position:absolute;left:72px;top:20px;font-size:25px">Sommaire</div>
  <div class="bebas front" style="position:absolute;left:0;top:50px;width:160px;height:7px;background:var(--blue);font-size:7px;line-height:7px;padding-left:72px">1/ Le sprint c'est quoi ?</div>
  <div class="tiny front" style="position:absolute;left:74px;top:59px">A/ Un concept innovant<br>B/ Partis-pris d'expertises reliées<br>C/ Livrables<br>D/ Experts</div>
  <div class="bebas front" style="position:absolute;left:0;top:83px;width:160px;height:7px;background:var(--red);font-size:7px;line-height:7px;padding-left:72px">2/ Process détaillé</div>
  <div class="tiny front" style="position:absolute;left:74px;top:92px">J-1 Questionnement préalable<br>Jour 1 : Vers un enrichissement<br>Jour 2 : La vision 360°<br>Jour 3 : Les leviers de transformation<br>Jour 4 : Transformer la façon<br>Jour 5 : On se lance !</div>
  <div class="bebas front" style="position:absolute;left:0;top:130px;width:160px;height:7px;background:var(--green);font-size:7px;line-height:7px;padding-left:72px">3/ Références des experts</div>
  <div class="brand">Tarnobe</div>
</section>

<section class="slide c4 r1">
  <div class="big-num">1</div>
  <div class="big-title" style="top:70px;left:94px">Le sprint<br>c'est quoi ?</div>
  <div class="brand">Tarnobe</div>
</section>

<!-- Row 2 -->
<section class="slide c1 r2">
  <div class="kicker">1 Le sprint c'est quoi ?</div>
  <div class="title">A/ Un concept<br>innovant:</div>
  <div class="row" style="left:17px;top:88px">
    <div class="box" style="width:38px;height:26px;background:var(--blue)">Conjugaison et high expertise</div>
    <div class="box" style="width:38px;height:26px;background:var(--red)">Avec efficacité</div>
    <div class="box" style="width:38px;height:26px;background:var(--orange)">Imaginer librement</div>
    <div class="box" style="width:38px;height:26px;background:var(--green)">Regarder autrement</div>
    <div class="box" style="width:38px;height:26px;background:var(--pink)">5 heures chrono</div>
    <div class="box" style="width:38px;height:26px;background:var(--magenta)">Proposer avec générosité</div>
  </div>
  <div class="brand">Tarnobe</div>
</section>

<section class="slide c2 r2">
  <div class="kicker">1 Le sprint c'est quoi ?</div>
  <div class="title" style="font-size:17px">B/ Partis-pris: une approche d'<br>expertises interconnectées</div>
  <div class="row" style="left:18px;top:82px;gap:26px">
    <div class="box" style="width:68px;height:30px;background:var(--blue)">Une vision pluridisciplinaire : SI, data, communication, intelligence collective</div>
    <div class="box" style="width:56px;height:30px;background:var(--green)">Un état d'esprit et des outils design thinking</div>
    <div class="box" style="width:68px;height:30px;background:var(--pink)">Une volonté farouche de présenter des solutions audacieuses et opérationnelles</div>
  </div>
  <svg style="position:absolute;left:86px;top:95px" width="150" height="6" aria-hidden="true"><path d="M0 3h24M94 3h24" stroke="#fff" stroke-width=".8"/></svg>
  <div class="brand">Tarnobe</div>
</section>

<section class="slide c3 r2">
  <div class="kicker">1 Le sprint c'est quoi ?</div>
  <div class="title">C/ Livrables</div>
  <div class="tiny" style="position:absolute;left:18px;top:58px;width:82px;font-size:4px">1/ Un état des lieux<br><br>2/ Mise en perspective de vos challenges digitaux stimulés par l'approche design thinking<br><br>3/ La mise en avant des points-clés sur lesquels se déterminer pour faire évoluer votre stratégie digitale en termes de :</div>
  <div class="bebas" style="position:absolute;left:146px;top:62px;font-size:7px;line-height:14px">
    <div><span style="color:var(--blue)">●</span> Excellence opérationnelle</div>
    <div><span style="color:var(--green)">■</span> Organisation du système d'information</div>
    <div><span style="color:var(--orange)">■</span> Stratégie data</div>
    <div><span style="color:var(--pink)">●</span> Communication digitale</div>
    <div><span style="color:var(--magenta)">●</span> Intelligence collective</div>
  </div>
  <div class="brand">Tarnobe</div>
</section>

<section class="slide c4 r2">
  <div class="kicker">1 Le sprint c'est quoi ?</div>
  <div class="title">D/ Experts</div>
  <div class="expert" style="left:16px;top:56px"><div class="photo" role="img" aria-label="Portrait de l'experte Claire Venant"></div><div class="tiny"><div class="expert-name">Claire Venant</div>#communication #innovation<br>Domaines : communication, RH, transformation, environnement interne<br>Challenge : accompagner la transformation des entreprises<br>Motto : l'adaptabilité avant tout</div></div>
  <div class="expert" style="left:146px;top:56px"><div class="photo" role="img" aria-label="Portrait de l'expert Marc Delorme"></div><div class="tiny"><div class="expert-name">Marc Delorme</div>#communication #transformation<br>Domaines : communication et stratégie, accompagnement du changement<br>Challenge : créer le lien entre les équipes<br>Motto : la valeur d'une idée tient à son usage</div></div>
  <div class="brand">Tarnobe</div>
</section>

<!-- Row 3 -->
<section class="slide c1 r3">
  <div class="kicker">1 Le sprint c'est quoi ?</div>
  <div class="title">D/ Experts</div>
  <div class="expert" style="left:16px"><div class="photo" role="img" aria-label="Portrait de l'expert Jean Luc Morvan"></div><div class="tiny"><div class="expert-name">Jean Luc Morvan</div>#stratégie #transformation<br>Domaines : entrepreneuriat, management, amélioration continue, recherche<br>Challenge : rendre ensemble la sphère humaine<br>Motto : si vous voulez aller vite, allez seul</div></div>
  <div class="expert" style="left:146px"><div class="photo" role="img" aria-label="Portrait de l'experte Élodie Ravel"></div><div class="tiny"><div class="expert-name">Élodie Ravel</div>#designthinking #intelligence<br>Domaines : design, architecture, entrepreneuriat, innovation<br>Challenge : relever les défis d'entreprise<br>Motto : il faut toujours viser la lune</div></div>
  <div class="brand">Tarnobe</div>
</section>

<section class="slide c2 r3">
  <div class="kicker">1 Le sprint c'est quoi ?</div>
  <div class="title">D/ Experts</div>
  <div class="expert" style="left:16px"><div class="photo" role="img" aria-label="Portrait de l'expert Hugo Lestrade"></div><div class="tiny"><div class="expert-name">Hugo Lestrade</div>#data #machinelearning #AI<br>Domaines : marketing, relation client, machine learning<br>Challenge : vous guider vers votre data<br>Motto : exploiter la donnée en projet</div></div>
  <div class="expert" style="left:146px"><div class="photo" role="img" aria-label="Portrait de l'expert Théo Marchal"></div><div class="tiny"><div class="expert-name">Théo Marchal</div>#stratégie #bigdata #cloud<br>Domaines : entrepreneuriat, coaching, stratégie SI, infrastructure<br>Challenge : rendre autonome votre SI<br>Motto : aligner la data sur la stratégie</div></div>
  <div class="brand">Tarnobe</div>
</section>

<section class="slide c3 r3">
  <div class="runner-area" role="img" aria-label="Illustration d'un coureur en facettes colorées" style="left:185px;top:24px;width:72px;height:118px"></div>
  <div class="kicker">1 Le sprint c'est quoi ?</div>
  <div class="title">D/ Experts</div>
  <div class="expert front" style="left:16px;width:150px"><div class="photo" role="img" aria-label="Portrait de l'expert Karim Belhadi"></div><div class="tiny"><div class="expert-name">Karim Belhadi</div>#architecture #cloud #agile<br>Domaines : architecture IT, accompagnement du changement, industrie<br>Challenge : vous apprendre comment développer vos nouvelles idées<br>Motto : le vrai voyage, c'est d'avoir de nouveaux yeux</div></div>
  <div class="brand">Tarnobe</div>
</section>

<section class="slide c4 r3">
  <div class="big-num" style="left:56px">2</div>
  <div class="big-title" style="top:62px;left:124px">Process<br>détaillé</div>
  <div class="brand">Tarnobe</div>
</section>

<!-- Row 4 -->
<section class="slide c1 r4">
  <div class="kicker">2/ Process détaillé</div>
  <div class="title" style="font-size:17px">Préparation du sprint:<br>questionnement client</div>
  <div class="bebas" style="position:absolute;left:18px;top:78px;font-size:42px;line-height:1;color:var(--lime)">?</div>
  <div style="position:absolute;left:43px;top:82px;font:700 6.5px/1.35 'Montserrat',sans-serif">Questionnement<br>préalable au sprint<div style="font-size:4.5px;color:var(--sky)">Envoi questionnaire client<br>par Tarnobe</div></div>
  <svg style="position:absolute;left:145px;top:80px" width="34" height="34" viewBox="0 0 34 34" aria-hidden="true"><g fill="none" stroke="var(--pink)" stroke-width="3"><circle cx="17" cy="17" r="14"/><circle cx="17" cy="17" r="7"/></g><circle cx="17" cy="17" r="2" fill="var(--pink)"/><path d="M17 17L31 3" stroke="var(--pink)" stroke-width="2"/></svg>
  <div style="position:absolute;left:186px;top:90px;font:700 6.5px/1.35 'Montserrat',sans-serif">Identification of<br>needs &amp; objectives</div>
  <div class="brand">Tarnobe</div>
</section>

<section class="slide c2 r4">
  <div class="kicker">2/ Process détaillé</div>
  <div class="title" style="font-size:17px">Jour 1 : vers un enrichissement<br>du questionnement</div>
  <div class="row" style="left:18px;top:78px;gap:22px">
    <div class="box" style="width:66px;height:24px;background:var(--blue);font:7px 'Bebas Neue',sans-serif">Besoins et objectifs du client</div>
    <div class="box" style="width:58px;height:24px;background:var(--green);font:7px 'Bebas Neue',sans-serif">Clarification des enjeux par Tarnobe</div>
    <div class="box" style="width:66px;height:24px;background:var(--pink);font:7px 'Bebas Neue',sans-serif">Questionnement client et point de vue augmenté</div>
  </div>
  <svg style="position:absolute;left:50px;top:88px" width="170" height="30" aria-hidden="true"><path d="M34 2h22M114 2h22M2 14v10h148v-10M76 14v10" stroke="#fff" stroke-width=".7" fill="none"/></svg>
  <div class="bebas" style="position:absolute;left:118px;top:118px;font-size:7px">Design thinking</div>
  <div class="brand">Tarnobe</div>
</section>

<section class="slide c3 r4">
  <div class="kicker">2/ Process détaillé</div>
  <div class="title" style="font-size:17px">Jour 2 : la vision 360°</div>
  <div class="row" style="left:16px;top:54px;gap:3px">
    <div class="box" style="width:48px;height:74px;background:var(--blue);align-items:flex-start;justify-content:flex-start;text-align:left;font-size:3.2px">État d'esprit collaboratif<br><br>• Compréhension du challenge<br>• Identification des parties prenantes</div>
    <div class="box" style="width:48px;height:74px;background:var(--red);align-items:flex-start;justify-content:flex-start;text-align:left;font-size:3.2px">Stratégie data<br><br>• Information des données<br>• Exploration de l'existant<br>• Plan d'actions</div>
    <div class="box" style="width:48px;height:74px;background:var(--orange);align-items:flex-start;justify-content:flex-start;text-align:left;font-size:3.2px">Excellence opérationnelle<br><br>• Analyse des processus<br>• Benchmark concurrentiel</div>
    <div class="box" style="width:48px;height:74px;background:var(--pink);align-items:flex-start;justify-content:flex-start;text-align:left;font-size:3.2px">Communication digitale<br><br>• Contribution des canaux<br>• Stratégie des images<br>• Territoires</div>
    <div class="box" style="width:48px;height:74px;background:var(--green);align-items:flex-start;justify-content:flex-start;text-align:left;font-size:3.2px">Organisation du système d'information<br><br>• Ressources<br>• Mise en commun<br>• Industrialisation</div>
  </div>
  <div class="brand">Tarnobe</div>
</section>

<section class="slide c4 r4">
  <div class="kicker">2/ Process détaillé</div>
  <div class="title" style="font-size:17px">Jour 3 : les leviers de<br>la transformation</div>
  <div class="bebas" style="position:absolute;left:18px;top:70px;width:246px;height:11px;background:var(--blue);font-size:8px;line-height:11px;text-align:center">Premières hypothèses de transformation</div>
  <div class="row" style="left:18px;top:86px;gap:4px">
    <div class="box" style="width:58px;height:34px;background:var(--red)">Agilité et amélioration continue</div>
    <div class="box" style="width:58px;height:34px;background:var(--orange)">Mash-up (inspiration sur les usages d'autres)</div>
    <div class="box" style="width:58px;height:34px;background:var(--magenta)">Anticipation sur les nouvelles technologies et applications (IA, IoT, bots…)</div>
    <div class="box" style="width:58px;height:34px;background:var(--green)">Les bonnes pratiques du marché</div>
  </div>
  <div class="brand">Tarnobe</div>
</section>

<!-- Row 5 -->
<section class="slide c1 r5">
  <div class="kicker">2/ Process détaillé</div>
  <div class="title" style="font-size:17px">Jour 4 : transformer la<br>façon dont on doit se transformer</div>
  <div class="row" style="left:14px;top:70px;gap:2px">
    <div class="box" style="width:33px;height:22px;background:var(--blue)">Focus impact clients</div>
    <div class="box" style="width:33px;height:22px;background:var(--blue)">Focus techno</div>
    <div class="box" style="width:33px;height:22px;background:var(--blue)">Focus data</div>
    <div class="box" style="width:33px;height:22px;background:var(--blue)">Focus excellence opérationnelle</div>
    <div class="box" style="width:33px;height:22px;background:var(--blue)">Focus talents</div>
    <div class="box" style="width:33px;height:22px;background:var(--blue)">Focus réalité économique</div>
    <div class="box" style="width:33px;height:22px;background:var(--purple)">Focus identité &amp; image</div>
  </div>
  <div class="bebas" style="position:absolute;left:14px;top:92px;width:246px;height:24px;background:var(--cyan);color:var(--blue);font-size:9.5px;line-height:24px;text-align:center">Pistes de solutions émergentes de la pluridisciplinarité</div>
  <div class="brand">Tarnobe</div>
</section>

<section class="slide c2 r5">
  <div class="kicker">2/ Process détaillé</div>
  <div class="title" style="top:30px;font-size:22px">Jour 5 : on se lance !</div>
  <div class="bebas" style="position:absolute;left:16px;top:62px;width:180px;height:10px;background:var(--blue);font-size:7.5px;line-height:10px;text-align:center">Présenter nos recommandations globales</div>
  <svg style="position:absolute;left:16px;top:72px" width="250" height="40" aria-hidden="true"><g stroke="#fff" stroke-width=".6"><path d="M22 0v8M68 0v8M114 0v8M160 0v8"/><path d="M183 28h8"/></g><path d="M189 26l3 2-3 2z" fill="#fff"/></svg>
  <div class="row" style="left:16px;top:82px;gap:4px">
    <div class="box" style="width:42px;height:30px;background:var(--red);font:6px 'Bebas Neue',sans-serif">Vos atouts, vos faiblesses</div>
    <div class="box" style="width:42px;height:30px;background:var(--orange);font:6px 'Bebas Neue',sans-serif">Vos urgences stratégiques</div>
    <div class="box" style="width:42px;height:30px;background:var(--green);font:6px 'Bebas Neue',sans-serif">Les quick wins</div>
    <div class="box" style="width:42px;height:30px;background:var(--pink);font:6px 'Bebas Neue',sans-serif">L'agenda, le budget, les prochains 18 mois</div>
  </div>
  <div class="box" style="position:absolute;left:224px;top:82px;width:36px;height:30px;background:var(--red);font:6px 'Bebas Neue',sans-serif">Vers une nouvelle ambition</div>
  <div class="brand">Tarnobe</div>
</section>

<section class="slide c3 r5">
  <div class="runner-area" role="img" aria-label="Illustration d'un coureur en facettes colorées" style="left:172px;top:20px;width:74px;height:122px"></div>
  <div class="kicker">2/ Process détaillé</div>
  <div class="title" style="top:30px;font-size:22px">Le jour d'après</div>
  <div class="front" style="position:absolute;left:14px;top:68px;width:150px;font:6.5px/1.4 'Montserrat',sans-serif">Capacité d'accompagnement opérationnelle sur l'ensemble des problématiques identifiées dans le sprint</div>
  <div class="brand">Tarnobe</div>
</section>

<section class="slide c4 r5">
  <div class="big-num" style="left:46px">3</div>
  <div class="big-title" style="left:112px;top:60px">Références<br>des experts</div>
  <div class="brand">Tarnobe</div>
</section>

<!-- Row 6 -->
<section class="slide c1 r6">
  <div class="kicker">3/ Références des experts</div>
  <div class="title" style="top:30px">Références des experts</div>
  <div class="refs" style="left:16px;top:58px;width:248px">
    <div><b>Aérolia :</b><span>De l'optimisation d'un positionnement de marque à la redéfinition des périmètres de responsabilité des communicants</span></div>
    <div><b>Vexa Vie Invest :</b><span>Coaching de l'équipe datascience, optimisation de l'effort commercial du réseau</span></div>
    <div><b>IREN :</b><span>Des valeurs à la création d'un manifeste identitaire partagé par les collaborateurs</span></div>
    <div><b>Hôpital Saint-Roch :</b><span>Définition d'une nouvelle politique de communication et d'engagement</span></div>
    <div><b>Norvia Telecom :</b><span>Formations intra-entreprise sur les solutions d'architectures big data</span></div>
    <div><b>Mutalis :</b><span>Coaching équipe data science et cartographie des axes de valorisation</span></div>
    <div><b>Interlia :</b><span>Diagnostic de performance du réseau commercial à partir des données</span></div>
  </div>
  <div class="brand">Tarnobe</div>
</section>

<section class="slide c2 r6">
  <div class="kicker">3/ Références des experts</div>
  <div class="title" style="top:30px">Références des experts</div>
  <div class="refs" style="left:16px;top:58px;width:248px">
    <div><b>Quorisk :</b><span>Enrichissement de leur offre produit pour en faire un outil de management de réseau</span></div>
    <div><b>Brightmoor :</b><span>Accompagnement d'une fusion et définition d'une stratégie de communication</span></div>
    <div><b>Cadrea :</b><span>Découverte du design thinking, développer la créativité de l'équipe</span></div>
    <div><b>Caisse Nationale d'Épargne :</b><span>Coaching design thinking pour un projet de candidature</span></div>
    <div><b>Bâtiva :</b><span>Coaching de design thinking pour plus de transversalité</span></div>
    <div><b>Bâtiva Construction :</b><span>Travail collaboratif avec des partenaires et des métiers</span></div>
    <div><b>Atelier RH :</b><span>Définition des besoins d'un outil de feedback interne</span></div>
    <div><b>Banque Lumière :</b><span>Mise en place de la nouvelle génération des centres d'appels</span></div>
  </div>
  <div class="brand">Tarnobe</div>
</section>

<section class="slide c3 r6">
  <div class="kicker">3/ Références des experts</div>
  <div class="title" style="top:30px">Références des experts</div>
  <div class="refs" style="left:16px;top:58px;width:248px">
    <div><b>Orbitis :</b><span>Réorganisation de l'entité produit de l'éditeur</span></div>
    <div><b>Assistia :</b><span>Médiation sociale et optimisation du parcours métier</span></div>
    <div><b>Telvéo :</b><span>Refonte des process métier de la cellule recours client</span></div>
    <div><b>Banque Centrale Régionale :</b><span>Architecture et mise en place de la plateforme d'intégration continue</span></div>
    <div><b>Matériaux Dufresne :</b><span>Optimisation des équipes Java/JEE</span></div>
    <div><b>Garantis :</b><span>Architecture applicative, tech lead</span></div>
    <div><b>Mutuelle du Bâtiment :</b><span>Expert Java/JEE, architecture applicative</span></div>
  </div>
  <div class="brand">Tarnobe</div>
</section>

<section class="slide c4 r6">
  <div class="quote" style="left:20px;top:58px;font-size:17.5px">« L'entreprise digitalisée, c'est quand<br>on ne parle plus du digital ! »</div>
  <div class="brand">Tarnobe</div>
</section>
</body>
</html>
```